Chic, award winning Billboard wanted

Our restaurant is a modern and chic restaurant with AWESOME service, Fresh seafood and aged steaks in Costa Rica (where great service is a rarity as well as refined cooking).
The restaurant is called Q Seafood & Grill, located in Manuel Antonio, Costa Rica
Our current marketing line is "Q is not fine dining, it's fantastic dining" Our colours are Pantone u498 blue and black as background
Go to our web site to see our style www.Qseafoodgrill.example
We have secured a 3.5 metre high by 9 metre wide billboard on the main highway and looking for an outstanding design to drive traffic to our business.
People associate Seafood too much with our restaurant, so we want to have our logo very present, but have the words "seafood"; "grill"; "aged steaks"; "lounge" kind of floating around the Z so that people don't associate our restaurant with only one type of food.
REMEMBER THIS BILLBOARD IS ON A MAIN HIGHWAY THAT PEOPLE ARE TRAVELLING AT 55 MILES PER HOUR!
check out our pelvanto for customer reviews: http://www.pelvanto.example/Restaurant_Review-g503817-d7260491-Reviews-Q_Seafood_Grill-Manuel_Antonio_National_Park_Province_of_Puntarenas.html
Target Market(s)
Travelling American & European Tourists to National Park,
Other font styles liked:
- Century Gothic
Requirements
Must have
- Want a fun and interesting billboard that engages people, not a static information "Logo, name, phone number"
- Needs to have phone number: 2555-0137
- Needs to have Pelvanto logo
Nice to have
- See attached ad done for a local magazine for the "look"

```html
<!DOCTYPE html>
<html lang="en">
<head>
<meta charset="utf-8">
<title>Q Seafood &amp; Grill – Fantastic Dining</title>
<link rel="stylesheet" href="https://fonts.googleapis.com/css2?family=Open+Sans:wght@400;600;700&display=swap">
<style>
  :root {
    --bg-deep: #02030a;
    --bg-glow: #0b1a6e;
    --brand-blue: #1b8fd2;
    --faint-blue: #14386e;
    --float-blue: #5d9fe0;
    --white: #ffffff;
    --ring: #cfd3da;
    --badge-green: #7fbf3f;
    --logo-frame: #3a3a3a;
  }
  html, body {
    margin: 0;
    padding: 0;
    width: 1200px;
    height: 466px;
    overflow: hidden;
    background: var(--bg-deep);
  }
  .billboard {
    position: relative;
    width: 1200px;
    height: 466px;
    overflow: hidden;
    font-family: "Open Sans", sans-serif;
    background:
      radial-gradient(ellipse 55% 80% at 62% 45%, var(--bg-glow) 0%, #050a35 45%, var(--bg-deep) 85%);
  }
  .backdrop-letter {
    position: absolute;
    left: 362px;
    top: 30px;
    margin: 0;
    font-size: 380px;
    line-height: 1;
    font-weight: 700;
    color: var(--faint-blue);
    opacity: 0.75;
  }
  .menu-word {
    position: absolute;
    margin: 0;
    font-size: 24px;
    line-height: 1;
    font-weight: 600;
    letter-spacing: 2px;
    text-transform: uppercase;
    color: var(--float-blue);
    opacity: 0.85;
  }
  .menu-word--seafood { left: 236px; top: 24px; }
  .menu-word--grill   { left: 600px; top: 62px; }
  .menu-word--steaks  { left: 402px; top: 112px; font-size: 20px; }
  .menu-word--lounge  { left: 478px; top: 430px; font-size: 20px; }

  .brand-box {
    position: absolute;
    left: 43px;
    top: 51px;
    width: 158px;
    height: 168px;
    background: #000;
    border: 2px solid var(--logo-frame);
    display: flex;
    align-items: center;
    justify-content: center;
    text-align: center;
    box-sizing: border-box;
    padding: 10px;
  }
  .brand-name {
    margin: 0;
    color: var(--white);
    font-size: 22px;
    font-weight: 600;
    line-height: 1.25;
  }
  .tagline-lead {
    position: absolute;
    left: 217px;
    top: 158px;
    margin: 0;
    color: var(--white);
    font-size: 54px;
    line-height: 1;
    font-weight: 400;
    white-space: nowrap;
  }
  .tagline-main {
    position: absolute;
    left: 45px;
    top: 233px;
    margin: 0;
    color: var(--brand-blue);
    font-size: 63px;
    line-height: 1;
    font-weight: 700;
    white-space: nowrap;
  }
  .review-badge {
    position: absolute;
    left: 64px;
    top: 335px;
    width: 117px;
    height: 114px;
    background: var(--badge-green);
    border-radius: 3px;
  }
  .call-line {
    position: absolute;
    left: 236px;
    top: 376px;
    margin: 0;
    color: var(--white);
    font-size: 41px;
    line-height: 1;
    font-weight: 700;
    white-space: nowrap;
  }
  .dish-ring {
    position: absolute;
    left: 0;
    top: 0;
  }
</style>
</head>
<body>
  <main class="billboard">
    <p class="backdrop-letter" aria-hidden="true">Q</p>

    <p class="menu-word menu-word--seafood">Seafood</p>
    <p class="menu-word menu-word--grill">Grill</p>
    <p class="menu-word menu-word--steaks">Aged Steaks</p>
    <p class="menu-word menu-word--lounge">Lounge</p>

    <div class="brand-box">
      <p class="brand-name">Q Seafood &amp; Grill</p>
    </div>

    <p class="tagline-lead">is Not Fine Dining,</p>
    <h1 class="tagline-main">It’s Fantastic Dining.</h1>

    <div class="review-badge" aria-label="Pelvanto review badge"></div>

    <p class="call-line">Call Us on 2555-0137</p>

    <svg class="dish-ring" width="1200" height="466" viewBox="0 0 1200 466">
      <defs>
        <radialGradient id="salad" cx="50%" cy="50%" r="50%">
          <stop offset="0" stop-color="#c9b07a"/><stop offset="1" stop-color="#5d6b2e"/>
        </radialGradient>
        <radialGradient id="lobster" cx="50%" cy="50%" r="50%">
          <stop offset="0" stop-color="#b0643a"/><stop offset="1" stop-color="#3a2418"/>
        </radialGradient>
        <radialGradient id="sandwich" cx="50%" cy="50%" r="50%">
          <stop offset="0" stop-color="#f1e8d6"/><stop offset="1" stop-color="#c9a36a"/>
        </radialGradient>
        <radialGradient id="ribs" cx="50%" cy="50%" r="50%">
          <stop offset="0" stop-color="#8c4a22"/><stop offset="1" stop-color="#3b2a1e"/>
        </radialGradient>
        <radialGradient id="lounge" cx="50%" cy="40%" r="55%">
          <stop offset="0" stop-color="#3b5bff"/><stop offset="1" stop-color="#0a0c2a"/>
        </radialGradient>
      </defs>

      <g class="ring-links" stroke="var(--ring)" stroke-width="5" fill="none">
        <polyline points="765,167 958,97 1099,218 992,369 796,348 765,167"/>
      </g>

      <g class="dish" role="img" aria-label="Photo of a grilled seafood salad platter">
        <circle cx="765" cy="167" r="76" fill="url(#salad)" stroke="var(--white)" stroke-width="5"/>
      </g>
      <g class="dish" role="img" aria-label="Photo of grilled lobster and steak">
        <circle cx="958" cy="97" r="78" fill="url(#lobster)" stroke="var(--white)" stroke-width="5"/>
      </g>
      <g class="dish" role="img" aria-label="Photo of a sandwich with fries">
        <circle cx="1099" cy="218" r="70" fill="url(#sandwich)" stroke="var(--white)" stroke-width="5"/>
      </g>
      <g class="dish" role="img" aria-label="Photo of glazed ribs with sauce">
        <circle cx="992" cy="369" r="78" fill="url(#ribs)" stroke="var(--white)" stroke-width="5"/>
      </g>
      <g class="dish" role="img" aria-label="Photo of the blue-lit lounge bar">
        <circle cx="796" cy="348" r="76" fill="url(#lounge)" stroke="var(--white)" stroke-width="5"/>
      </g>
    </svg>
  </main>
</body>
</html>
```